Marolina Swimming & Athletics Center

We need Business Card for a Athletics center
The logo frome the Uploaded Files ( b card fimal)
Οn one side of card we need the logo of company the Contact and the website:
1. Address:(Limassol, Cyprus 12-14 Dravelonos str,Ano Feralia,P.C. 5280)

2.Phone number: (+357) 25-804273

3. Mail: info@marolinasport.example

3. Website: www.marolinasport.example

Οn the other side of the card we need to write the sport of the company:

1. Artistic Gymnastics
2. Swimming
3. Gym - Fitness
4. Programs
5. Dancing
5.Tennis

From the Uploaded Files you can get the logo.In a logo is behind the black color which can be removed from logo.

Υou can use that color you want.
.

Industry/Entity Type

Business

Font styles to use
Decorative

Colors
0555a3
ffcf3e
3176b5
0692cd
add136
f04a50
000000
cfcfcf
9d9d9d

Requirements
Should not have
• photos with faces
• photo fro the Website:www.marolinasport.example

```html
<!DOCTYPE html>
<html lang="en">
<head>
<meta charset="utf-8">
<title>Marolina Swimming &amp; Athletics Center – Business Card</title>
<link rel="stylesheet" href="https://fonts.googleapis.com/css2?family=Big+Shoulders+Stencil+Display:wght@700;800&family=Fredoka:wght@500&display=swap">
<style>
  :root {
    --page: #f4f3f1;
    --card-black: #0d0d0d;
    --card-dark: #1e1e1e;
    --amber: #f2a72c;
    --amber-deep: #d98c12;
    --white: #ffffff;
    --silver: #cfcfcf;
    --grey: #9d9d9d;
  }
  * { margin: 0; padding: 0; box-sizing: border-box; }
  html, body { width: 1200px; height: 1000px; overflow: hidden; }
  body { background: var(--page); position: relative; font-family: "Fredoka", sans-serif; }

  .card { position: absolute; width: 714px; height: 407px; overflow: hidden; }

  /* Front side */
  .card-front {
    left: 40px; top: 80px;
    background: radial-gradient(ellipse at 50% 45%, #2e2e2e 0%, #151515 55%, var(--card-black) 100%);
  }
  .splash { position: absolute; }
  .splash-left {
    left: 0; top: 0; width: 170px; height: 300px;
    background: radial-gradient(ellipse at 30% 35%, rgba(242,167,44,.75) 0%, rgba(242,167,44,.35) 40%, rgba(207,207,207,.15) 60%, transparent 75%);
  }
  .splash-right {
    right: 0; top: 0; width: 150px; height: 330px;
    background: radial-gradient(ellipse at 60% 40%, rgba(207,207,207,.7) 0%, rgba(242,167,44,.45) 40%, rgba(242,167,44,.15) 60%, transparent 78%);
  }
  .splash-bottom {
    left: 165px; bottom: 0; width: 110px; height: 30px;
    background: radial-gradient(ellipse at 50% 100%, rgba(242,167,44,.6) 0%, rgba(207,207,207,.3) 45%, transparent 75%);
  }

  .brand-mark {
    position: absolute; left: 306px; top: 32px;
    width: 104px; height: 104px; border-radius: 50%;
    border: 4px solid var(--white); background: var(--card-black);
  }
  .brand-name {
    position: absolute; left: 0; width: 714px; top: 154px;
    text-align: center;
    font-family: "Big Shoulders Stencil Display", sans-serif;
    font-weight: 800; font-size: 120px; line-height: 1;
    letter-spacing: 1px; color: var(--amber);
  }

  .contact-address {
    position: absolute; left: 16px; top: 310px;
    display: flex; align-items: center; gap: 14px;
  }
  .contact-address p {
    color: var(--amber); font-size: 14px; line-height: 26px;
    text-transform: uppercase; letter-spacing: .2px;
  }
  .contact-list { position: absolute; left: 410px; top: 293px; list-style: none; }
  .contact-list li {
    display: flex; align-items: center; height: 38px;
    color: var(--amber); font-size: 16px; white-space: nowrap;
  }
  .contact-list svg { width: 46px; flex: none; margin-right: 16px; }

  /* Back side */
  .card-back {
    left: 444px; top: 535px;
    background: repeating-linear-gradient(45deg, #232323 0 2px, #1a1a1a 2px 4px);
  }
  .back-frame {
    position: absolute; left: 11px; top: 10px; right: 11px; bottom: 11px;
    border: 6px solid var(--amber);
  }
  .sport-art {
    position: absolute; left: 478px; top: 25px; width: 220px; height: 360px;
    background: linear-gradient(160deg, rgba(157,157,157,.55) 0%, rgba(207,207,207,.25) 45%, rgba(242,167,44,.35) 75%, rgba(255,255,255,.45) 100%);
    border-radius: 40px 0 0 40px;
  }
  .sport-list {
    position: absolute; left: 146px; top: 64px; list-style: none;
  }
  .sport-list li {
    display: flex; align-items: center; height: 53px;
    font-family: "Big Shoulders Stencil Display", sans-serif;
    font-weight: 800; font-size: 41px; color: var(--white);
    text-transform: uppercase; letter-spacing: -2px; white-space: nowrap;
  }
  .sport-list svg { width: 38px; height: 38px; margin-right: 10px; flex: none; }
</style>
</head>
<body>

<section class="card card-front" aria-label="Business card front">
  <div class="splash splash-left" role="img" aria-label="Orange and white paint splatter decoration"></div>
  <div class="splash splash-right" role="img" aria-label="White and orange paint splatter decoration"></div>
  <div class="splash splash-bottom" role="img" aria-label="Small paint splatter decoration"></div>

  <div class="brand-mark" aria-hidden="true"></div>
  <h1 class="brand-name">MAROLINA</h1>

  <div class="contact-address">
    <svg width="36" height="50" viewBox="0 0 36 50" aria-hidden="true">
      <path d="M18 0C8 0 0 8 0 18c0 13 18 32 18 32s18-19 18-32C36 8 28 0 18 0z" fill="var(--amber)"/>
      <circle cx="18" cy="17" r="7" fill="var(--card-black)"/>
    </svg>
    <p>Limassol, Cyprus 12-14 Dravelonos str,<br>Ano Feralia,<br>P.C. 5280</p>
  </div>

  <ul class="contact-list">
    <li>
      <svg viewBox="0 0 46 30" height="30" aria-hidden="true">
        <path d="M6 3c3-2 6-1 8 2l3 5c1 2 0 4-2 5l-2 1c2 5 6 9 11 11l1-2c1-2 3-3 5-2l5 3c3 2 3 5 1 8-3 4-9 4-17-2S3 16 3 10c0-3 1-5 3-7z" fill="var(--amber)"/>
      </svg>
      <span>(+357) 25-804273</span>
    </li>
    <li>
      <svg viewBox="0 0 46 30" height="30" aria-hidden="true">
        <text x="23" y="25" text-anchor="middle" font-family="Fredoka, sans-serif" font-size="32" fill="var(--amber)">@</text>
      </svg>
      <span>info@marolinasport.example</span>
    </li>
    <li>
      <svg viewBox="0 0 46 30" height="30" aria-hidden="true">
        <g fill="none" stroke="var(--amber)" stroke-width="2.2">
          <circle cx="28" cy="15" r="12"/>
          <ellipse cx="28" cy="15" rx="5" ry="12"/>
          <line x1="16" y1="15" x2="40" y2="15"/>
          <line x1="18" y1="9" x2="38" y2="9"/>
          <line x1="18" y1="21" x2="38" y2="21"/>
        </g>
      </svg>
      <span>www.marolinasport.example</span>
    </li>
  </ul>
</section>

<section class="card card-back" aria-label="Business card back">
  <div class="back-frame"></div>
  <div class="sport-art" role="img" aria-label="Silhouettes of a dancer, gymnast, tennis racket, chequered flag and stars"></div>
  <ul class="sport-list">
    <li><svg viewBox="0 0 24 24" aria-hidden="true"><path d="M12 1l3.2 7 7.6.7-5.7 5 1.7 7.5L12 17.3 5.2 21.2l1.7-7.5-5.7-5 7.6-.7z" fill="var(--white)"/></svg>Artistic Gymnastics</li>
    <li><svg viewBox="0 0 24 24" aria-hidden="true"><path d="M12 1l3.2 7 7.6.7-5.7 5 1.7 7.5L12 17.3 5.2 21.2l1.7-7.5-5.7-5 7.6-.7z" fill="var(--white)"/></svg>Swimming</li>
    <li><svg viewBox="0 0 24 24" aria-hidden="true"><path d="M12 1l3.2 7 7.6.7-5.7 5 1.7 7.5L12 17.3 5.2 21.2l1.7-7.5-5.7-5 7.6-.7z" fill="var(--white)"/></svg>Gym - Fitness</li>
    <li><svg viewBox="0 0 24 24" aria-hidden="true"><path d="M12 1l3.2 7 7.6.7-5.7 5 1.7 7.5L12 17.3 5.2 21.2l1.7-7.5-5.7-5 7.6-.7z" fill="var(--white)"/></svg>Programs</li>
    <li><svg viewBox="0 0 24 24" aria-hidden="true"><path d="M12 1l3.2 7 7.6.7-5.7 5 1.7 7.5L12 17.3 5.2 21.2l1.7-7.5-5.7-5 7.6-.7z" fill="var(--white)"/></svg>Dancing</li>
    <li><svg viewBox="0 0 24 24" aria-hidden="true"><path d="M12 1l3.2 7 7.6.7-5.7 5 1.7 7.5L12 17.3 5.2 21.2l1.7-7.5-5.7-5 7.6-.7z" fill="var(--white)"/></svg>Tennis</li>
  </ul>
</section>

</body>
</html>
```